Stylish yet Funky Poster

We are a hair and beauty salon and have won some awards recently that we would like to display winning images in our window fronts.
Our windows are 900mm wide, 2100mm high. We have high res images and need to add some text somewhere on the image.
Salon colours are green, white though perhaps using black would be OK too.
I would like the text to read:-
2010 National Vello Shade Cup Winner
2010 Qld Vello Shade Cup Winner
(text as large as possible)

Model by Lou Parnell - (this text can be smaller)

The image is important but the more important purpose of the poster is to let passers by know about the competition wins.
Updates

Hi I've uploaded a new Dovria Logo which should be more clear.

I have uploaded bauhaus font also

Target Market(s)

Our target market are ladies 25 - 55 years old, mostly professional women.

Industry/Entity Type

Beauty Salon

Requirements
Must have
• Be 900mm wide, 2100mm high
• Must include supplied image.
• Must include text: 2010 National Vello Shade Cup Winner,
• 2010 Qld Vello Shade Cup Winner
• Model by Lou Parnell
Nice to have
• Salon name - Fernwick Hair & Beauty
• We also won 2008 National Vello Shade Cup too - this may be used on same banner
• Background can be changed
• Either black or white version of Dovria logo attached

```html
<!DOCTYPE html>
<html lang="en">
<head>
<meta charset="utf-8">
<title>Fernwick Hair &amp; Beauty – 2010 Trophy Winners</title>
<link rel="stylesheet" href="https://fonts.googleapis.com/css2?family=Archivo+Black&family=Roboto+Condensed:wght@300;400;700&display=swap">
<style>
  :root {
    --paper: #ffffff;
    --ink-light: #ffffff;
    --salon-green: #3ddc2a;
    --plum-deep: #1a0913;
    --plum-mid: #3d1531;
    --night: #050304;
    --magenta: #b23a86;
    --magenta-soft: #d86fb3;
    --photo-rose: #7a1c3a;
    --photo-shadow: #2a0c18;
    --wave-grey: #6d6a70;
  }
  * { margin: 0; padding: 0; box-sizing: border-box; }
  html, body {
    width: 1200px; height: 2800px; overflow: hidden; background: var(--paper);
  }
  .poster {
    position: relative; width: 1200px; height: 2800px; overflow: hidden;
    background: var(--paper);
    font-family: "Roboto Condensed", "Arial Narrow", sans-serif;
    color: var(--ink-light);
  }
  .model-photo {
    position: absolute; left: 0; top: 0; width: 620px; height: 1060px;
    background:
      radial-gradient(ellipse 50% 28% at 45% 18%, var(--photo-rose), transparent 75%),
      radial-gradient(ellipse 60% 40% at 42% 72%, var(--photo-shadow), transparent 80%),
      linear-gradient(90deg, #efe6ea 0%, #f3edf0 70%, var(--paper) 100%);
  }
  .backdrop { position: absolute; inset: 0; width: 1200px; height: 2800px; }
  .salon-name {
    position: absolute; right: 70px; top: 80px; width: 400px;
    text-align: center; color: var(--salon-green);
    font-weight: 700; font-size: 70px; line-height: 1.05;
  }
  .headline { position: absolute; left: 0; width: 1200px; line-height: 1; white-space: nowrap; }
  .year {
    top: 990px; text-align: center; padding-left: 120px;
    font-family: "Archivo Black", sans-serif; font-size: 370px;
  }
  .trophy {
    top: 1300px; text-align: right; padding-right: 72px;
    font-weight: 400; font-size: 150px;
  }
  .winners {
    top: 1420px; text-align: center; padding-left: 120px;
    font-family: "Archivo Black", sans-serif; font-size: 218px;
  }
  .award {
    text-align: right; padding-right: 72px;
    font-weight: 300; font-size: 116px;
  }
  .award-national { top: 1690px; }
  .award-state { top: 1830px; }
  .earlier-win {
    top: 2010px; text-align: right; padding-right: 100px;
    font-weight: 300; font-size: 58px; line-height: 1.25;
  }
  .model-credit {
    position: absolute; left: 40px; bottom: 22px;
    font-weight: 700; font-size: 40px;
  }
  .partner-name {
    position: absolute; right: 90px; bottom: 110px;
    font-weight: 300; font-size: 110px; line-height: 1;
  }
</style>
</head>
<body>
<main class="poster">
  <div class="model-photo" role="img" aria-label="Award-winning model with a sleek burgundy asymmetric bob, wearing a black ruffled halter top"></div>

  <svg class="backdrop" viewBox="0 0 1200 2800" aria-hidden="true">
    <defs>
      <linearGradient id="night-fill" x1="0" y1="0" x2="0" y2="1">
        <stop offset="0" stop-color="var(--plum-mid)"/>
        <stop offset="0.35" stop-color="var(--plum-deep)"/>
        <stop offset="1" stop-color="var(--night)"/>
      </linearGradient>
      <linearGradient id="swoosh-fill" x1="0" y1="0" x2="1" y2="0">
        <stop offset="0" stop-color="var(--magenta-soft)" stop-opacity="0.9"/>
        <stop offset="0.6" stop-color="var(--magenta)"/>
        <stop offset="1" stop-color="var(--plum-mid)"/>
      </linearGradient>
      <radialGradient id="glow" cx="0.5" cy="0.5" r="0.5">
        <stop offset="0" stop-color="var(--magenta-soft)" stop-opacity="0.55"/>
        <stop offset="1" stop-color="var(--magenta-soft)" stop-opacity="0"/>
      </radialGradient>
    </defs>
    <path class="dark-field" d="M0 1080 C 380 980, 780 880, 1200 800 L1200 2800 L0 2800 Z" fill="url(#night-fill)"/>
    <path class="magenta-swoosh" d="M0 1010 C 400 900, 800 790, 1200 720 L1200 810 C 800 860, 400 960, 0 1110 Z" fill="url(#swoosh-fill)" opacity="0.85"/>
    <circle class="light-glow" cx="1000" cy="1260" r="260" fill="url(#glow)"/>
    <path class="lower-wave" d="M0 2560 C 300 2490, 700 2620, 1200 2520" fill="none" stroke="var(--wave-grey)" stroke-width="6" opacity="0.6"/>
    <path class="lower-wave" d="M0 2600 C 320 2530, 720 2660, 1200 2560" fill="none" stroke="var(--wave-grey)" stroke-width="3" opacity="0.4"/>
  </svg>

  <p class="salon-name">Fernwick Hair &amp; Beauty</p>

  <h1>
    <span class="headline year">2010</span>
    <span class="headline trophy">trophy</span>
    <span class="headline winners">winners</span>
  </h1>
  <p class="headline award award-national">National Vello Shade</p>
  <p class="headline award award-state">Qld Vello Shade</p>
  <p class="headline earlier-win">also winners of the<br>2008 National Vello Shade Cup</p>

  <p class="partner-name">Dovria</p>
  <p class="model-credit">model by Lou Parnell</p>
</main>
</body>
</html>
```